TAMBERLY DISTRIBUTION VAN SIGNAGE

We would like a design done for our range of vans: the first van to be wrapped/logo'd will be a light grey corvane hauler if you wish to use this as template van. I have included our company logo( we do not need this redesigned) We like the design to be simple yet modern and funky. We need the Tamberly logo to be prominant. Other Details to include:

The phone number: +442847751932
Email: info@tamberly-example.eu.
Website: www.tamberly-example.eu

Target Market(s)

Retail stores

Font styles to use
Sans Serif

```html
<!DOCTYPE html>
<html lang="en">
<head>
<meta charset="utf-8">
<title>Tamberly Distribution – Van Side Wrap</title>
<link href="https://fonts.googleapis.com/css2?family=Josefin+Sans:wght@300;400;600;700&display=swap" rel="stylesheet">
<style>
  :root {
    --backdrop: #bcbfbe;
    --wrap-white: #e6e6ea;
    --charcoal: #3d3d3d;
    --ink: #111111;
    --white: #ffffff;
  }
  html, body {
    margin: 0;
    padding: 0;
    width: 1200px;
    height: 610px;
    overflow: hidden;
    background: var(--backdrop);
  }
  .wrap-artwork {
    display: block;
    width: 1200px;
    height: 610px;
    font-family: "Josefin Sans", sans-serif;
  }
  .side-panel { fill: var(--wrap-white); }
  .brand-field { fill: var(--charcoal); }
  .orbit-line { fill: none; stroke: var(--ink); stroke-width: 3; }
  .web-address {
    fill: var(--ink);
    font-weight: 700;
    font-size: 28px;
    letter-spacing: 1.5px;
  }
  .contact-band { fill: var(--charcoal); }
  .icon-tile { fill: var(--white); }
  .icon-glyph { fill: var(--ink); }
  .icon-flap { fill: none; stroke: var(--white); stroke-width: 2; }
  .contact-text {
    fill: var(--white);
    font-weight: 600;
    font-size: 30px;
    letter-spacing: 1px;
  }
  .brand-name {
    fill: var(--white);
    font-weight: 400;
    font-size: 52px;
    letter-spacing: 5px;
  }
  .brand-tagline {
    fill: var(--white);
    font-weight: 300;
    font-size: 19px;
    letter-spacing: 5px;
  }
</style>
</head>
<body>
<svg class="wrap-artwork" viewBox="0 0 1200 610" xmlns="http://www.w3.org/2000/svg">
  <defs>
    <clipPath id="panel-shape">
      <rect x="40" y="60" width="1120" height="490" rx="24"/>
    </clipPath>
    <path id="address-arc" d="M 720.5 70 A 312 312 0 0 0 788 530"/>
  </defs>

  <g clip-path="url(#panel-shape)">
    <rect class="side-panel" x="40" y="60" width="1120" height="490"/>

    <circle class="brand-field" cx="960" cy="270" r="282"/>
    <rect class="brand-field" x="960" y="60" width="200" height="490"/>

    <circle class="orbit-line" cx="960" cy="270" r="345"/>

    <text class="web-address">
      <textPath href="#address-arc" startOffset="3%">WWW.TAMBERLY-EXAMPLE.EU</textPath>
    </text>
  </g>

  <g class="contact-row">
    <path class="contact-band" d="M 60 318 L 545 318 Q 585 318 598 373 L 75 373 Q 68 340 60 318 Z"/>
    <rect class="icon-tile" x="84" y="312" width="46" height="48" rx="6"/>
    <path class="icon-glyph" d="M 96 324 q 4 -3 7 0 l 4 6 q 1 3 -2 5 l -2 2 q 3 6 9 9 l 2 -2 q 2 -3 5 -2 l 6 4 q 3 3 0 7 l -3 2 q -8 3 -20 -9 q -12 -12 -9 -20 z"/>
    <text class="contact-text" x="146" y="356">+442847751932</text>
  </g>

  <g class="contact-row">
    <path class="contact-band" d="M 60 385 L 545 385 Q 585 385 598 440 L 75 440 Q 68 407 60 385 Z"/>
    <rect class="icon-tile" x="84" y="379" width="46" height="48" rx="6"/>
    <rect class="icon-glyph" x="92" y="393" width="30" height="21" rx="1"/>
    <path class="icon-flap" d="M 93 394 L 107 406 L 121 394"/>
    <text class="contact-text" x="146" y="423">info@tamberly-example.eu</text>
  </g>

  <text class="brand-name" x="965" y="290" text-anchor="middle">TAMBERLY</text>
  <text class="brand-tagline" x="965" y="330" text-anchor="middle">DISTRIBUTION</text>
</svg>
</body>
</html>
```